依頼詳細
今回の案件は、封筒(長3と角2)のデザインになります。
※茶封筒の予定(白でも可)
記載項目
上記 記載事項を参照
希望イメージ
シンプル 複雑
単色 カラフル
暗い 明るい
日常 高級
遊び心 厳粛
未来的 伝統的
女性的 男性的
希望する色
設定なし
納品ファイル
• イラストレーター形式 (.ai)
• PNG形式 (.png)
補足説明
設定なし
※アイコンの参考URL
https://zerubi-kata.example/40817-symbol-a/

https://zerubikata.example/52390-symbol-b/
アイコンのURLがリンク切れでした。失礼しました。

https://zerubi-kata.example/52390-symbol-b/
ご提案ありがとうございます。
もう少し斬新で、アーステックな感じに振ってもいい気がしました。
(抽象的になりますが…)

参考になるものがあれば、添付いたします。
参考URL
https://www.senmoku.example/30452/download_details/view/2641/
https://velmora-works.example/dtp/futo/
https://www.kuralin.example/showcase/kuralin/

こちらが全てというわけでなく、こういったテイストが好みという風に
受け取ってください。
■ 選んだ理由

シンプルでまとまっていたと思います。

■ 提案者全員のお礼・コメント

今回もたくさんのご提案をいただき、ありがとうございました。

```html
<!DOCTYPE html>
<html lang="ja">
<head>
<meta charset="utf-8">
<title>NOVA TRACE 角2封筒</title>
<link rel="stylesheet" href="https://fonts.googleapis.com/css2?family=Oswald:wght@300;500&family=Noto+Sans+JP:wght@400;500&display=swap">
<style>
  :root {
    --paper: #ffffff;
    --page: #ffffff;
    --edge: #bfbfbf;
    --ink: #3d3d3d;
    --ink-soft: #6a6a6a;
    --accent: #d8435f;
    --rule: #c8c8c8;
  }
  * { margin: 0; padding: 0; box-sizing: border-box; }
  html, body { width: 849px; height: 1200px; overflow: hidden; background: var(--page); }
  .envelope { position: relative; width: 849px; height: 1200px; }
  .envelope-outline { position: absolute; inset: 0; }
  .tagline {
    position: absolute;
    left: 700px; top: 226px;
    writing-mode: vertical-rl;
    font-family: "Oswald", sans-serif;
    font-weight: 300;
    font-size: 38px;
    letter-spacing: 10.5px;
    color: var(--ink);
    line-height: 1;
    white-space: nowrap;
  }
  .tagline-emphasis { color: var(--accent); font-weight: 500; }
  .address-rule {
    position: absolute; left: 340px; top: 538px;
    width: 268px; height: 1px; background: var(--rule);
  }
  .sender { position: absolute; left: 170px; top: 926px; font-family: "Noto Sans JP", sans-serif; color: var(--ink); }
  .brand { display: flex; align-items: center; gap: 10px; }
  .brand-dot { width: 20px; height: 20px; border-radius: 50%; background: var(--accent); }
  .brand-name {
    font-family: "Oswald", sans-serif; font-weight: 500;
    font-size: 20px; letter-spacing: 1.5px; color: var(--accent);
  }
  .company { margin-top: 10px; font-size: 10.5px; font-weight: 500; letter-spacing: 0.5px; }
  .offices { display: flex; gap: 22px; margin-top: 10px; }
  .office { font-size: 9px; line-height: 1.6; color: var(--ink-soft); width: 190px; }
  .office-label {
    display: inline-block; font-size: 8px; color: var(--ink);
    border: 1px solid var(--ink-soft); padding: 0 5px; margin-bottom: 3px;
  }
</style>
</head>
<body>
<main class="envelope">
  <svg class="envelope-outline" width="849" height="1200" viewBox="0 0 849 1200" aria-hidden="true">
    <path d="M108 147 L124 50 Q126 42 136 42 L713 42 Q723 42 725 50 L741 147" fill="var(--paper)" stroke="var(--edge)" stroke-width="1.5"/>
    <rect x="105" y="147" width="637" height="1008" fill="var(--paper)" stroke="var(--edge)" stroke-width="1.5"/>
  </svg>

  <p class="tagline">SHAPE A QUIET FUTURE WITH <span class="tagline-emphasis">INTENT</span></p>

  <div class="address-rule"></div>

  <section class="sender">
    <div class="brand">
      <span class="brand-dot"></span>
      <span class="brand-name">NOVA TRACE</span>
    </div>
    <p class="company">株式会社 NOVA TRACE</p>
    <div class="offices">
      <div class="office">
        <span class="office-label">名古屋本社</span><br>
        〒460-0099<br>
        名古屋市中区栄架空町1丁目2番3号<br>
        サンプル栄ビル4階<br>
        TEL 052-000-1234　FAX 052-000-5678
      </div>
      <div class="office">
        <span class="office-label">東京本社</span><br>
        〒150-0099<br>
        東京都渋谷区架空台2丁目5番8号<br>
        サンプル渋谷ビル3F02号室<br>
        TEL 03-0000-2468　FAX 050-0000-1357
      </div>
    </div>
  </section>
</main>
</body>
</html>
```